Vorlan cards

I am in the auto motive, transportation business I would like a business card that is Something cool, modern edgy, having to do with car culture. I offer towing service for high and exotic cars. I also provide towing for collisions and car accidents. I offer open and enclosed transport nationwide.

Target Market(s)

Car culture people high end auto collectors

Industry/Entity Type

Towing car carrier

Contact Information for Business Card

My company colors black yellow and silver

Font styles to use
Serif

```html
<!DOCTYPE html>
<html lang="en">
<head>
<meta charset="UTF-8">
<title>Vorlan Cards</title>
<link rel="stylesheet" href="https://fonts.googleapis.com/css2?family=Raleway:wght@400;500;600&display=swap">
<style>
  :root {
    --ink: #050505;
    --paper: #ffffff;
    --yellow: #f5c41c;
    --silver: #d9d9d9;
    --backdrop: #8a8a8a;
  }
  * { margin: 0; padding: 0; box-sizing: border-box; }
  html, body { width: 1200px; height: 1200px; overflow: hidden; }
  body {
    background: var(--backdrop);
    font-family: "Raleway", sans-serif;
    position: relative;
  }
  .card {
    position: absolute;
    width: 760px;
    height: 434px;
    border-radius: 28px;
    overflow: hidden;
    box-shadow: 0 14px 30px rgba(0,0,0,0.35);
  }
  .card-front { left: 220px; top: 90px; background: var(--paper); }
  .card-back {
    left: 220px; top: 620px;
    background: radial-gradient(circle at 50% 50%, #2a2a2a 0%, #111 45%, var(--ink) 100%);
  }
  .front-bands { position: absolute; inset: 0; width: 100%; height: 100%; }
  .brand {
    position: absolute;
    display: flex;
    align-items: center;
    gap: 14px;
    font-weight: 600;
    text-transform: uppercase;
    letter-spacing: 2px;
  }
  .brand-square { width: 22px; height: 22px; background: var(--yellow); }
  .card-front .brand { left: 250px; top: 92px; font-size: 44px; color: var(--ink); }
  .card-back .brand {
    left: 0; right: 0; top: 0; bottom: 0;
    justify-content: center;
    font-size: 78px; color: var(--silver);
  }
  .holder {
    position: absolute;
    left: 70px; bottom: 58px;
    padding-left: 22px;
    border-left: 4px solid var(--yellow);
  }
  .holder-name { color: var(--yellow); font-size: 38px; font-weight: 500; letter-spacing: 1px; line-height: 1.05; }
  .holder-role { color: var(--paper); font-size: 18px; letter-spacing: 1px; margin-top: 4px; }
  .contacts {
    position: absolute;
    right: 48px; bottom: 70px;
    list-style: none;
    color: var(--paper);
    font-size: 21px;
  }
  .contacts li { display: flex; align-items: center; gap: 14px; margin-top: 10px; }
  .contacts svg { width: 24px; height: 24px; flex: none; }
</style>
</head>
<body>

<section class="card card-front">
  <svg class="front-bands" viewBox="0 0 760 434" preserveAspectRatio="none" aria-hidden="true">
    <polygon points="0,320 760,170 760,434 0,434" fill="var(--yellow)"/>
    <polygon points="0,332 760,182 760,434 0,434" fill="var(--ink)"/>
  </svg>
  <div class="brand"><span class="brand-square"></span>Vorlan</div>

  <div class="holder">
    <div class="holder-name">JOHN DOE</div>
    <div class="holder-role">POSITION</div>
  </div>

  <ul class="contacts">
    <li>
      <svg viewBox="0 0 24 24"><path fill="var(--yellow)" d="M6.6 10.8a15 15 0 0 0 6.6 6.6l2.2-2.2c.3-.3.7-.4 1-.2 1.1.4 2.3.6 3.6.6.6 0 1 .4 1 1V20c0 .6-.4 1-1 1A17 17 0 0 1 3 4c0-.6.4-1 1-1h3.5c.6 0 1 .4 1 1 0 1.3.2 2.5.6 3.6.1.3 0 .7-.2 1z"/></svg>
      (000) 000 0000
    </li>
    <li>
      <svg viewBox="0 0 24 24"><rect x="2" y="5" width="20" height="14" fill="var(--yellow)"/><path d="M2 5l10 8 10-8" fill="none" stroke="var(--ink)" stroke-width="1.6"/></svg>
      email@youremail.com
    </li>
    <li>
      <svg viewBox="0 0 24 24" fill="none" stroke="var(--yellow)" stroke-width="1.8"><circle cx="12" cy="12" r="9.5"/><ellipse cx="12" cy="12" rx="4" ry="9.5"/><path d="M2.5 12h19M4 7h16M4 17h16"/></svg>
      www.yourwebsite.com
    </li>
  </ul>
</section>

<section class="card card-back">
  <div class="brand"><span class="brand-square"></span>Vorlan</div>
</section>

</body>
</html>
```